Orthopaedic Clinic Needs facebook page

Orthopaedic Clinic needs facebook page. The name of our clinic is Larchmont Orthopaedics. We focus on hip and knee orthopaedic conditions, as well as general orthopaedics. The main services are total knee replacements, total hip replacements, sports injury of the knee, hip fractures. Unique selling points of our service would be 1. Patient Centred Care, 2. Value Driven, 3. 2 Double-Fellowship Trained Surgeons.

Colour scheme should fit the logo design and be within the general colour recommendations of a medical clinic.

The design should be modern, eye catching, draws the end user to the website.

We would like to design our facebook page for future social media marketing.
In accordance with local advertisement regulations pertaining to medical clinics, no statements must have any information or laudatory statements such as the use of best, better, breakthrough, champions, or any statements that imply superiority and that may create unjustified expectations of services.

Target Market(s)

Patients
Friends family and relatives of patients.

Font styles to use
Serif
Sans Serif

Requirements
Must have
• My project must have my logo.

A nice colour scheme comfortable to the eye.
Nice to have
• Nice eye catching design that will draw the end user to the page.
Should not have
• Must not have any information that create unjustified expectaions.
Must not contain laudatory statements such as best, better, breakthrough, champions, or other statement that may create unjustified expecation of services.

```html
<!DOCTYPE html>
<html lang="en">
<head>
<meta charset="utf-8">
<title>Larchmont Orthopaedics – Cover</title>
<link rel="stylesheet" href="https://fonts.googleapis.com/css2?family=Exo+2:wght@400&family=Orbitron:wght@600&display=swap">
<style>
  :root {
    --teal: #5bb8ae;
    --slate: #4a5561;
    --slate-text: #55606b;
    --frame: #8a939b;
    --paper: #f5f6f7;
    --white: #ffffff;
    --photo-light: #eef2f4;
    --photo-mid: #c9d9e2;
    --photo-blue: #6fa6c4;
  }
  * { box-sizing: border-box; margin: 0; padding: 0; }
  html, body { width: 1200px; height: 444px; overflow: hidden; background: var(--paper); }
  .cover { position: relative; width: 1200px; height: 444px; overflow: hidden; background: var(--paper); }

  .cover__photo {
    position: absolute; left: 540px; top: 0; width: 660px; height: 444px;
    background:
      radial-gradient(ellipse 140px 130px at 370px 230px, rgba(111,166,196,0.55), transparent 70%),
      linear-gradient(90deg, var(--paper) 0%, var(--photo-light) 30%, var(--photo-mid) 70%, #d8e2e8 100%);
  }

  .brand { position: absolute; left: 22px; top: 16px; display: flex; align-items: flex-start; }
  .brand__mark { width: 112px; height: 116px; background: var(--teal); border-radius: 10px; }
  .brand__name {
    margin-left: 28px; font-family: "Exo 2", sans-serif; font-weight: 400;
    color: var(--slate-text); text-transform: uppercase; line-height: 1;
  }
  .brand__line1 { display: block; font-size: 66px; letter-spacing: 1px; margin-top: 4px; }
  .brand__line2 { display: block; font-size: 33px; letter-spacing: 12.5px; margin-top: 16px; }

  .pill {
    position: absolute; height: 38px; border: 3px solid var(--teal); border-radius: 10px;
    background: var(--slate); color: var(--white);
    font-family: "Orbitron", sans-serif; font-weight: 600; font-size: 19px;
    display: flex; align-items: center; justify-content: center; text-transform: uppercase;
    letter-spacing: 0.5px; white-space: nowrap;
  }
  .pill__accent { color: var(--teal); margin-right: 0.35em; }
  .pill--fellowship { left: 22px; top: 152px; width: 620px; }
  .pill--value { left: 22px; top: 200px; width: 228px; }
  .pill--care { left: 258px; top: 200px; width: 360px; }

  .services {
    position: absolute; left: 53px; top: 274px; width: 405px; height: 128px;
    border: 2px solid var(--frame); border-radius: 8px;
  }
  .services__title {
    position: absolute; left: 26px; top: -15px; padding: 0 5px; background: var(--paper);
    font-family: "Exo 2", sans-serif; font-size: 25px; color: var(--teal); letter-spacing: 1px; line-height: 1;
  }
  .services__list { list-style: none; position: absolute; left: 16px; top: 22px; }
  .services__item {
    display: flex; align-items: center; height: 23.5px;
    font-family: "Exo 2", sans-serif; font-size: 18px; color: var(--slate-text);
    letter-spacing: 1px; text-transform: uppercase;
  }
  .services__item::before {
    content: ""; width: 7px; height: 7px; border-radius: 50%; background: var(--teal); margin-right: 10px;
  }
</style>
</head>
<body>
  <main class="cover">
    <div class="cover__photo" role="img" aria-label="Photo of a patient in a knee brace walking on crutches beside a physiotherapist in a rehab room"></div>

    <header class="brand">
      <div class="brand__mark"></div>
      <h1 class="brand__name">
        <span class="brand__line1">Larchmont</span>
        <span class="brand__line2">Orthopaedics</span>
      </h1>
    </header>

    <div class="pill pill--fellowship"><span class="pill__accent">Double Fellowship</span>Trained Surgeons</div>
    <div class="pill pill--value"><span class="pill__accent">Value</span>Drive</div>
    <div class="pill pill--care"><span class="pill__accent">Patient Centred</span>Care</div>

    <section class="services">
      <h2 class="services__title">SERVICES</h2>
      <ul class="services__list">
        <li class="services__item">Total Knee Replacements</li>
        <li class="services__item">Total Hip Replacements</li>
        <li class="services__item">Sports Injury of the Knee</li>
        <li class="services__item">Hip Fractures</li>
      </ul>
    </section>
  </main>
</body>
</html>
```